Personal Brand (Influencer) Website

I'm looking for a brand new website design for a youtuber/influencer Dane Whitaker.

I'm looking for a sleek design that is visually appealing while still maintaining full functionality and user experience.

Here is our current website: http://danewhitakerhq.example/

I want to combine some of the best elements and designs from the following websites.

https://www.milofenwright.example/
https://www.renzovale.example/
https://quinnbarlow.example/
https://www.silasmerrow.example/
http://danewhitakerhq.example/
http://www.kenfrayle.example/

Here are the different tabs that I would need designed as well as the main page:

Home Page (main page)
Blogs
My story (about me)
Top 100 book list
Contact

Here are several links and social media handles for you to get a better gauge on the branding of Dane Whitaker:
https://www.videohub.example/channel/XQpar3k9v-T2mhZZ_QWrta7z
https://trend-rocket.example/market-blog/uncategorized/dane-whitaker-entrepreneur-winning-market-follow-data-ep-17/
https://danelisten2.pagepath.example/optin-48203917
https://www.snapgrid.example/officialdanewhitaker/

```html
<!DOCTYPE html>
<html lang="en">
<head>
<meta charset="utf-8">
<title>Dane Whitaker — Live Life On Your Terms</title>
<link href="https://fonts.googleapis.com/css2?family=Signika:wght@400;600&family=Questrial&display=swap" rel="stylesheet">
<style>
  :root {
    --ink-dark: #333333;
    --brand-blue: #1a8ad8;
    --hero-blue: #2a7fc4;
    --white: #ffffff;
    --soft-gray: #f2f2f2;
    --body-text: #444444;
    --muted: #666666;
    --nav-text: #555555;
  }
  * { margin: 0; padding: 0; box-sizing: border-box; }
  html, body { width: 1200px; height: 2500px; overflow: hidden; }
  body { position: relative; background: var(--white); font-family: "Questrial", sans-serif; color: var(--body-text); }
  .block { position: absolute; left: 0; width: 1200px; }

  .top-bar { top: 0; height: 103px; background: var(--ink-dark); display: flex; align-items: center; justify-content: center; }
  .brand-mark { display: flex; align-items: center; gap: 10px; font-family: "Signika", sans-serif; font-weight: 600; font-size: 28px; letter-spacing: 3px; color: var(--white); }
  .brand-mark .dot { width: 22px; height: 22px; background: var(--brand-blue); }

  .main-nav { top: 103px; height: 54px; background: var(--white); border-bottom: 1px solid #e4e4e4; }
  .main-nav ul { position: absolute; left: 62px; top: 0; height: 54px; display: flex; align-items: center; list-style: none; }
  .main-nav li { font-size: 14px; letter-spacing: .5px; color: var(--nav-text); padding: 0 20px; border-left: 1px solid #d8d8d8; line-height: 18px; }
  .main-nav li:first-child { border-left: none; padding-left: 16px; color: var(--brand-blue); }
  .social-links { position: absolute; right: 44px; top: 0; height: 54px; display: flex; align-items: center; gap: 12px; font-size: 12px; color: var(--nav-text); }
  .social-links span + span { border-left: 1px solid #d8d8d8; padding-left: 12px; }

  .hero { top: 157px; height: 603px; overflow: hidden; }
  .hero-photo { position: absolute; inset: 0; background: linear-gradient(180deg, #2a86cf 0%, #4d9ad6 40%, #3a82c2 70%, #2a6fb0 100%); }
  .hero-diamond { position: absolute; left: 495px; top: 140px; width: 210px; height: 210px; transform: rotate(45deg); background: rgba(255,255,255,.18); border: 2px solid rgba(255,255,255,.25); }
  .hero-title { position: absolute; top: 160px; width: 100%; text-align: center; font-family: "Signika", sans-serif; font-weight: 600; font-size: 58px; color: var(--white); letter-spacing: 1px; text-shadow: 0 2px 6px rgba(0,0,0,.25); }
  .hero-tagline { position: absolute; top: 248px; width: 100%; text-align: center; font-size: 29px; color: var(--white); }
  .signup-lead { position: absolute; top: 428px; width: 100%; text-align: center; font-size: 22px; color: var(--white); }
  .signup-form { position: absolute; top: 485px; left: 183px; display: flex; gap: 12px; }
  .signup-field { width: 312px; height: 46px; background: rgba(255,255,255,.3); color: var(--white); font-size: 13px; padding: 15px 22px; }
  .signup-button { width: 187px; height: 46px; margin-left: 0; background: var(--white); color: var(--brand-blue); font-family: "Signika", sans-serif; font-weight: 600; font-size: 21px; display: flex; align-items: center; justify-content: center; letter-spacing: .5px; }

  .about { top: 760px; height: 542px; background: linear-gradient(90deg, #cfcfcf 0%, #e6e6e6 55%, #eeeeee 100%); overflow: hidden; }
  .about-portrait { position: absolute; left: 0; top: 0; width: 430px; height: 542px; background: linear-gradient(160deg, #8a8a8a 0%, #555 45%, #2e2e2e 100%); }
  .about-copy { position: absolute; left: 547px; top: 85px; width: 585px; }
  .section-heading { font-family: "Signika", sans-serif; font-weight: 600; font-size: 40px; color: var(--brand-blue); line-height: 1.3; }
  .about-copy p { font-size: 14.5px; line-height: 25px; color: #333; margin-top: 10px; }
  .about-copy .section-heading { margin-bottom: 8px; }
  .cta-button { display: inline-flex; align-items: center; justify-content: center; height: 45px; width: 187px; background: var(--brand-blue); color: var(--white); font-family: "Signika", sans-serif; font-weight: 600; font-size: 21px; letter-spacing: .5px; }
  .about-copy .cta-button { margin-top: 22px; }

  .course { top: 1302px; height: 541px; background: var(--soft-gray); }
  .course-copy { position: absolute; left: 78px; top: 128px; width: 560px; }
  .course-intro { font-style: italic; font-size: 17px; color: #444; margin-top: 14px; }
  .course-copy p.detail { font-size: 13.5px; line-height: 25px; color: var(--muted); margin-top: 12px; }
  .course-copy .cta-button { margin-top: 22px; }
  .course-badge { position: absolute; left: 683px; top: 52px; }

  .recent-posts { top: 1843px; height: 512px; background: var(--white); }
  .recent-posts .section-heading { position: absolute; top: 45px; width: 100%; text-align: center; }
  .post-card { position: absolute; top: 117px; width: 500px; height: 312px; }
  .post-card.first { left: 78px; background: linear-gradient(135deg, #1c2040 0%, #3a2a5a 50%, #1a1a30 100%); }
  .post-card.second { left: 623px; background: linear-gradient(135deg, #161616 0%, #2b2b2b 50%, #1e2a44 100%); }
  .post-card svg { position: absolute; left: 212px; top: 118px; }

  .site-footer { top: 2355px; height: 145px; background: var(--ink-dark); color: var(--white); text-align: center; }
  .footer-links { margin-top: 42px; font-size: 15px; }
  .footer-links span + span::before { content: "|"; margin: 0 12px; }
  .copyright { margin-top: 26px; font-size: 14px; }
</style>
</head>
<body>
  <header class="block top-bar">
    <div class="brand-mark"><span class="dot"></span>DANE WHITAKER</div>
  </header>

  <nav class="block main-nav">
    <ul>
      <li>HOME</li><li>BLOG</li><li>MT STORY</li><li>TOP 100 BOOKS</li><li>CONTACT</li>
    </ul>
    <div class="social-links"><span>Friendbook</span><span>Snapgrid</span><span>Videohub</span></div>
  </nav>

  <section class="block hero">
    <div class="hero-photo" role="img" aria-label="Snowy mountain range under a blue tint"></div>
    <div class="hero-diamond"></div>
    <h1 class="hero-title">DANE WHITAKER</h1>
    <p class="hero-tagline">Live Life On Your Terms</p>
    <p class="signup-lead">Sign up for the latest videos &amp; free content.</p>
    <div class="signup-form">
      <div class="signup-field">Your Name</div>
      <div class="signup-field">Your Email</div>
      <div class="signup-button">GET STARTED</div>
    </div>
  </section>

  <section class="block about">
    <div class="about-portrait" role="img" aria-label="Black and white portrait of Dane Whitaker in a cap with a backpack on a mountain"></div>
    <div class="about-copy">
      <h2 class="section-heading">Meet Dane Whitaker</h2>
      <p>Dane Whitaker is a 7 figure Ecommerce Entrepreneur, Speaker, Inventor, Bio-hacker, and Positive thinker. He believes the world is getting better every day.</p>
      <p>Dane went from 0 to 6 Million in 6 Months selling Eclipse Glasses on Marketbay Fulfilled. He also proposed to his wife in Outer Space.</p>
      <p>Dane Whitaker has been an entrepreneur since he was 12 years old. His journey began by selling on Realm Of Quests Auction House. Dane strategically skipped school &amp; stayed up all night to play video games- not because he was an obsessed pre-teen, but because he knew acquiring valuable gears was easier during these times. The more weapons he had, the more money he'd make.</p>
      <span class="cta-button">KNOW MORE</span>
    </div>
  </section>

  <section class="block course">
    <div class="course-copy">
      <h2 class="section-heading">The First Free Marketbay Private Label Course</h2>
      <p class="course-intro">I am giving away everything that I know for free.</p>
      <p class="detail">Myself &amp; the top Marketbay sellers will be teaching you everything that you need to know about creating &amp; managing a thriving Marketbay Fulfilled Business so that you can live your life on your terms.</p>
      <span class="cta-button">SIGN UP HERE</span>
    </div>
    <svg class="course-badge" width="420" height="420" viewBox="0 0 420 420">
      <defs>
        <clipPath id="badge-clip"><circle cx="210" cy="210" r="200"/></clipPath>
        <linearGradient id="scene-fill" x1="0" y1="0" x2="0" y2="1">
          <stop offset="0" stop-color="#5d7a4a"/><stop offset="1" stop-color="#6e6258"/>
        </linearGradient>
      </defs>
      <circle cx="210" cy="210" r="208" fill="var(--brand-blue)"/>
      <g clip-path="url(#badge-clip)">
        <rect x="0" y="0" width="420" height="420" fill="var(--brand-blue)"/>
        <path d="M0 170 Q210 60 420 150 L420 420 L0 420 Z" fill="url(#scene-fill)" role="img" aria-label="Hiker seated on rocks beside a mountain stream"/>
      </g>
      <circle cx="210" cy="210" r="188" fill="none" stroke="#ffffff" stroke-width="6"/>
      <circle cx="210" cy="210" r="206" fill="none" stroke="#ffffff" stroke-width="3"/>
      <text x="210" y="92" text-anchor="middle" fill="#fff" font-family="Questrial, sans-serif" font-size="16">Live Life On Your Terms With My</text>
      <text x="210" y="122" text-anchor="middle" fill="#fff" font-family="Questrial, sans-serif" font-size="16">Free Marketbay Private Label Course</text>
    </svg>
  </section>

  <section class="block recent-posts">
    <h2 class="section-heading">Recent Posts</h2>
    <div class="post-card first" role="img" aria-label="Video thumbnail comparing product discovery tools">
      <svg width="76" height="76" viewBox="0 0 76 76"><circle cx="38" cy="38" r="34" fill="none" stroke="#fff" stroke-width="4"/><path d="M30 24 L54 38 L30 52 Z" fill="#fff"/></svg>
    </div>
    <div class="post-card second" role="img" aria-label="Video thumbnail about starting an online store with a small budget">
      <svg width="76" height="76" viewBox="0 0 76 76"><circle cx="38" cy="38" r="34" fill="none" stroke="#fff" stroke-width="4"/><path d="M30 24 L54 38 L30 52 Z" fill="#fff"/></svg>
    </div>
  </section>

  <footer class="block site-footer">
    <div class="footer-links"><span>Home</span><span>Blog</span><span>My History</span><span>Top 100 Books</span><span>Contact</span></div>
    <p class="copyright">2018 ©DANE WHITAKER- All Rights Reserved.</p>
  </footer>
</body>
</html>
```